App Design

This is a 'video player' app - will be used to stream video files and watch them on a device. Need 3/4 skins for user customization.
Design will need to be versatile - used on: Kestrel4/4S/5 and vexTab2/3
Require an app design that shows the required functionality described by us, allows ease to navigate and visually creates a unique user experience.
App must have following pages: (refer to attached pages)
1. Search Page
2. Results Page
3. Video Page
4. End Page
3-4 skins for user preference
important: if you are interested please submit designs by tomorrow night - we will be picking from submitted designs - will make revisions and finalize the design within 4-5 days.
timing is crucial- please only submit if you can commit to timeline and design requirements. There will be refinements required.
Please see the attached update.
Additional reference files have been added to help in your efforts.
We have added a sample design that may help with your submissions. Please see brief
Target Market(s)
early adapters for technology / kestrel, tablet, zorbix users
Requirements
Should not have
- should not be generic design

```html
<!DOCTYPE html>
<html lang="en">
<head>
<meta charset="utf-8">
<title>Video Player App – Screens</title>
<link href="https://fonts.googleapis.com/css2?family=Open+Sans:wght@400;600;700&family=Lobster&display=swap" rel="stylesheet">
<style>
:root{
  --bg-top:#10182a;
  --bg-bottom:#24324e;
  --screen-black:#000;
  --blue-light:#5ab8e8;
  --blue:#2a8fd6;
  --blue-dark:#1766b0;
  --accent:#2a9ae0;
  --text-white:#ffffff;
  --panel:#e6e6e6;
  --panel-dark:#cfcfcf;
  --card:#f7f7f7;
  --ink:#333;
  --muted:#666;
  --tab:#2b2b2b;
  --tab-active:#4a4a4a;
  --green:#6bd12b;
}
*{box-sizing:border-box;margin:0;padding:0}
html,body{width:1200px;height:1000px;overflow:hidden}
body{font-family:"Open Sans",Arial,sans-serif;background:linear-gradient(180deg,var(--bg-top),var(--bg-bottom))}
.canvas{position:relative;width:1200px;height:1000px;overflow:hidden}

.screen{position:absolute;top:195px;width:331px;height:587px;background:var(--screen-black)}
.screen--splash{left:46px}
.screen--grid{left:436px}
.screen--list{left:827px}

.status-bar{height:22px;display:flex;align-items:center;padding:0 6px;color:var(--text-white);font-weight:700;font-size:13px;position:relative}
.status-bar .signal{display:flex;align-items:flex-end;gap:1px;margin-right:4px}
.status-bar .signal i{display:block;width:2px;background:#fff}
.status-bar .carrier{letter-spacing:.2px}
.status-bar .net{margin-left:9px}
.status-bar .lock{position:absolute;left:50%;margin-left:-10px;top:4px}
.status-bar .battery{position:absolute;right:8px;top:6px;width:22px;height:10px;border:1px solid #fff;border-radius:2px;padding:1px}
.status-bar .battery::before{content:"";display:block;height:100%;background:#fff}

.toggle{position:absolute;width:60px;height:26px;border-radius:13px;background:linear-gradient(#2e4b5e,#476a80);box-shadow:inset 0 1px 3px rgba(0,0,0,.5)}
.toggle .tick{position:absolute;left:5px;top:3px}
.toggle .knob{position:absolute;right:1px;top:1px;width:24px;height:24px;border-radius:50%;background:linear-gradient(#fff,#cfcfcf);box-shadow:0 1px 2px rgba(0,0,0,.4);font-size:6px;color:#999;text-align:center;line-height:24px}

/* splash */
.splash{position:absolute;top:22px;left:0;width:331px;height:565px;border-radius:10px;overflow:hidden;background:linear-gradient(180deg,#4aa6dc 0%,#2a86cc 50%,#1a6fbd 100%)}
.splash .toggle{left:253px;top:12px}
.splash-logo{position:absolute;top:100px;left:0;width:100%;text-align:center;font-size:66px;font-weight:700;color:#f2f2f2;letter-spacing:-1px}
.splash-text{position:absolute;top:214px;left:18px;right:18px;text-align:center;color:#f2f6fa;font-size:13px;line-height:17px;letter-spacing:-.35px}

/* shared header */
.app-header{position:absolute;top:22px;left:0;width:331px;height:46px;background:linear-gradient(180deg,#5cb6ea,#2a8ad6 60%,#1e75c4);border-radius:8px 8px 0 0}
.app-header h1{font-family:"Lobster",cursive;font-weight:400;font-size:25px;color:#f4f4f4;text-align:center;line-height:44px;text-shadow:0 2px 2px rgba(0,0,0,.35)}
.app-header .toggle{left:264px;top:9px}
.search-band{position:absolute;top:68px;left:0;width:331px;height:43px;background:linear-gradient(#e9e9e9,#d8d8d8);box-shadow:0 3px 5px rgba(0,0,0,.35);z-index:2}
.search-field{position:absolute;left:12px;top:8px;width:306px;height:24px;border-radius:5px;background:linear-gradient(#c8c8c8,#d6d6d6);box-shadow:inset 0 1px 2px rgba(0,0,0,.35);display:flex;align-items:center;padding-left:8px;font-size:9.5px;color:#777}
.search-field svg{margin-right:10px}
.search-field.filled{color:#444}

/* grid */
.grid-body{position:absolute;top:111px;left:0;width:331px;height:476px;background:var(--panel)}
.video-grid{position:absolute;top:16px;left:16px;display:grid;grid-template-columns:139px 139px;column-gap:21px;row-gap:0}
.grid-item{height:154px}
.thumb-frame{width:139px;height:110px;background:#fafafa;padding:5px;box-shadow:0 1px 3px rgba(0,0,0,.35)}
.grid-item .title{margin-top:5px;font-size:11px;font-weight:700;color:var(--accent);white-space:nowrap}
.grid-item .meta{display:flex;justify-content:space-between;font-size:6px;font-weight:600;color:#444;margin-top:1px}

.photo{position:relative;width:100%;height:100%}
.photo .badge{position:absolute;top:5px;width:11px;height:10px;background:var(--accent);display:flex;align-items:center;justify-content:center}
.photo .badge.like{left:3px}
.photo .badge.chat{left:3px;top:19px}
.photo .duration{position:absolute;top:5px;right:3px;background:var(--accent);color:#fff;font-size:6.5px;font-weight:700;padding:1px 3px}
.photo .play{position:absolute;left:50%;top:50%;width:28px;height:28px;margin:-14px 0 0 -14px;background:rgba(42,154,224,.9);display:flex;align-items:center;justify-content:center}
.photo.small .play{width:22px;height:22px;margin:-11px 0 0 -11px}

.ph-sea{background:linear-gradient(180deg,#6c9fd4 0%,#b9cfe3 45%,#8da0ad 62%,#6b6a5c 80%,#4b4636 100%)}
.ph-road{background:linear-gradient(180deg,#a0522a 0%,#c97a36 35%,#b78a55 60%,#d5b88e 100%)}
.ph-kitchen{background:linear-gradient(180deg,#8a6e52 0%,#c2a579 40%,#d8cda2 65%,#e6e0d3 100%)}
.ph-stage{background:linear-gradient(180deg,#f2f2f0 0%,#e4e2dc 45%,#b8503e 70%,#3a5a34 100%)}
.ph-portrait{background:linear-gradient(180deg,#4e6877 0%,#7c8d94 45%,#5c6f86 75%,#3b4c60 100%)}
.ph-window{background:linear-gradient(180deg,#cbd6de 0%,#e9eef1 40%,#7c9aa8 70%,#2a3a44 100%)}

/* list */
.list-body{position:absolute;top:111px;left:0;width:331px;height:426px;background:var(--panel);overflow:hidden}
.list-item{position:absolute;left:4px;width:321px;height:96px;background:var(--card);box-shadow:0 1px 3px rgba(0,0,0,.3)}
.list-item .photo{position:absolute;left:4px;top:4px;width:114px;height:88px}
.list-item .copy{position:absolute;left:124px;top:3px;right:6px}
.list-item h2{font-size:10px;font-weight:700;color:var(--accent)}
.list-item p{font-size:7.5px;font-weight:600;color:var(--accent);line-height:10px;margin-top:3px}
.list-item .by{font-size:6.5px;font-weight:700;color:#333;margin-top:8px}
.list-item .stats{position:absolute;left:124px;bottom:5px;display:flex;gap:6px}
.list-item .stat{height:11px;background:#b8b8b8;border-radius:1px;font-size:5px;color:#333;display:flex;align-items:center;gap:3px;padding:0 5px}

.tab-bar{position:absolute;top:537px;left:0;width:331px;height:50px;background:linear-gradient(#3a3a3a,#1e1e1e);display:flex;border-top:1px solid #555}
.tab{flex:1;display:flex;flex-direction:column;align-items:center;justify-content:flex-end;padding-bottom:5px;gap:5px;color:#eee;font-size:7.5px;font-weight:600;border-right:1px solid #111;white-space:nowrap}
.tab:last-child{border-right:0}
.tab.active{background:linear-gradient(#555,#3f3f3f);margin-top:-6px;border-radius:4px 4px 0 0}
</style>
</head>
<body>
<div class="canvas">

  <!-- Splash screen -->
  <section class="screen screen--splash">
    <div class="status-bar">
      <span class="signal"><i style="height:3px"></i><i style="height:4px"></i><i style="height:5px"></i><i style="height:6px"></i><i style="height:7px"></i></span>
      <span class="carrier">QUIVEL</span><span class="net">3G</span>
      <svg class="lock" width="10" height="12" viewBox="0 0 10 12"><path d="M2.5 5V3.5a2.5 2.5 0 0 1 5 0V5" fill="none" stroke="#fff" stroke-width="1.5"/><rect x="1" y="5" width="8" height="7" rx="1" fill="#fff"/></svg>
      <span class="battery"></span>
    </div>
    <div class="splash">
      <div class="toggle"><svg class="tick" width="20" height="20" viewBox="0 0 20 20"><path d="M3 10l5 5 9-11" fill="none" stroke="var(--green)" stroke-width="4" stroke-linecap="round"/></svg><span class="knob">‹ ›</span></div>
      <div class="splash-logo">Logo</div>
      <p class="splash-text">Lorem ipsum dolor sit amet, consectetur adipi-<br>sicing elit, sed do eiusmod tempor incididunt ut<br>labore et dolore magna aliqua.</p>
    </div>
  </section>

  <!-- Grid results screen -->
  <section class="screen screen--grid">
    <div class="status-bar">
      <span class="signal"><i style="height:3px"></i><i style="height:4px"></i><i style="height:5px"></i><i style="height:6px"></i><i style="height:7px"></i></span>
      <span class="carrier">QUIVEL</span><span class="net">3G</span>
      <svg class="lock" width="10" height="12" viewBox="0 0 10 12"><path d="M2.5 5V3.5a2.5 2.5 0 0 1 5 0V5" fill="none" stroke="#fff" stroke-width="1.5"/><rect x="1" y="5" width="8" height="7" rx="1" fill="#fff"/></svg>
      <span class="battery"></span>
    </div>
    <header class="app-header">
      <h1>App Name</h1>
      <div class="toggle"><svg class="tick" width="20" height="20" viewBox="0 0 20 20"><path d="M3 10l5 5 9-11" fill="none" stroke="var(--green)" stroke-width="4" stroke-linecap="round"/></svg><span class="knob">‹ ›</span></div>
    </header>
    <div class="search-band">
      <div class="search-field"><svg width="11" height="11" viewBox="0 0 11 11"><circle cx="4.5" cy="4.5" r="3.5" fill="none" stroke="#555" stroke-width="1.4"/><path d="M7 7l3.5 3.5" stroke="#555" stroke-width="1.6"/></svg>Search</div>
    </div>
    <div class="grid-body">
      <div class="video-grid">
        <article class="grid-item">
          <div class="thumb-frame"><div class="photo ph-sea" role="img" aria-label="Video thumbnail: bicycle on a beach under a blue sky">
            <span class="badge like"><svg width="7" height="6" viewBox="0 0 10 9"><path d="M5 9L1 5a2.5 2.5 0 0 1 4-3 2.5 2.5 0 0 1 4 3z" fill="#fff"/></svg></span>
            <span class="badge chat"><svg width="7" height="6" viewBox="0 0 10 9"><ellipse cx="5" cy="4" rx="4.5" ry="3.5" fill="#fff"/></svg></span>
            <span class="duration">4.06</span>
            <span class="play"><svg width="12" height="14" viewBox="0 0 12 14"><path d="M1 1l10 6-10 6z" fill="#fff"/></svg></span>
          </div></div>
          <div class="title">Lorem Ipsum dolor ism....</div>
          <div class="meta"><span>By Norvel</span><span>3 week ago</span></div>
        </article>
        <article class="grid-item">
          <div class="thumb-frame"><div class="photo ph-road" role="img" aria-label="Video thumbnail: autumn path through trees">
            <span class="badge like"><svg width="7" height="6" viewBox="0 0 10 9"><path d="M5 9L1 5a2.5 2.5 0 0 1 4-3 2.5 2.5 0 0 1 4 3z" fill="#fff"/></svg></span>
            <span class="badge chat"><svg width="7" height="6" viewBox="0 0 10 9"><ellipse cx="5" cy="4" rx="4.5" ry="3.5" fill="#fff"/></svg></span>
            <span class="duration">3.36</span>
            <span class="play"><svg width="12" height="14" viewBox="0 0 12 14"><path d="M1 1l10 6-10 6z" fill="#fff"/></svg></span>
          </div></div>
          <div class="title">Lorem Ipsum dolor ism....</div>
          <div class="meta"><span>By Norvel</span><span>3 week ago</span></div>
        </article>
        <article class="grid-item">
          <div class="thumb-frame"><div class="photo ph-kitchen" role="img" aria-label="Video thumbnail: two cooks in a kitchen">
            <span class="badge like"><svg width="7" height="6" viewBox="0 0 10 9"><path d="M5 9L1 5a2.5 2.5 0 0 1 4-3 2.5 2.5 0 0 1 4 3z" fill="#fff"/></svg></span>
            <span class="badge chat"><svg width="7" height="6" viewBox="0 0 10 9"><ellipse cx="5" cy="4" rx="4.5" ry="3.5" fill="#fff"/></svg></span>
            <span class="duration">4.06</span>
            <span class="play"><svg width="12" height="14" viewBox="0 0 12 14"><path d="M1 1l10 6-10 6z" fill="#fff"/></svg></span>
          </div></div>
          <div class="title">Lorem Ipsum dolor ism....</div>
          <div class="meta"><span>By Norvel</span><span>3 week ago</span></div>
        </article>
        <article class="grid-item">
          <div class="thumb-frame"><div class="photo ph-stage" role="img" aria-label="Video thumbnail: performer among colourful chairs">
            <span class="badge like"><svg width="7" height="6" viewBox="0 0 10 9"><path d="M5 9L1 5a2.5 2.5 0 0 1 4-3 2.5 2.5 0 0 1 4 3z" fill="#fff"/></svg></span>
            <span class="badge chat"><svg width="7" height="6" viewBox="0 0 10 9"><ellipse cx="5" cy="4" rx="4.5" ry="3.5" fill="#fff"/></svg></span>
            <span class="duration">3.36</span>
            <span class="play"><svg width="12" height="14" viewBox="0 0 12 14"><path d="M1 1l10 6-10 6z" fill="#fff"/></svg></span>
          </div></div>
          <div class="title">Lorem Ipsum dolor ism....</div>
          <div class="meta"><span>By Norvel</span><span>3 week ago</span></div>
        </article>
        <article class="grid-item">
          <div class="thumb-frame"><div class="photo ph-portrait" role="img" aria-label="Video thumbnail: portrait of a person in denim">
            <span class="badge like"><svg width="7" height="6" viewBox="0 0 10 9"><path d="M5 9L1 5a2.5 2.5 0 0 1 4-3 2.5 2.5 0 0 1 4 3z" fill="#fff"/></svg></span>
            <span class="badge chat"><svg width="7" height="6" viewBox="0 0 10 9"><ellipse cx="5" cy="4" rx="4.5" ry="3.5" fill="#fff"/></svg></span>
            <span class="duration">4.06</span>
            <span class="play"><svg width="12" height="14" viewBox="0 0 12 14"><path d="M1 1l10 6-10 6z" fill="#fff"/></svg></span>
          </div></div>
          <div class="title">Lorem Ipsum dolor ism....</div>
          <div class="meta"><span>By Norvel</span><span>3 week ago</span></div>
        </article>
        <article class="grid-item">
          <div class="thumb-frame"><div class="photo ph-window" role="img" aria-label="Video thumbnail: figure behind a window grid">
            <span class="badge like"><svg width="7" height="6" viewBox="0 0 10 9"><path d="M5 9L1 5a2.5 2.5 0 0 1 4-3 2.5 2.5 0 0 1 4 3z" fill="#fff"/></svg></span>
            <span class="badge chat"><svg width="7" height="6" viewBox="0 0 10 9"><ellipse cx="5" cy="4" rx="4.5" ry="3.5" fill="#fff"/></svg></span>
            <span class="duration">3.36</span>
            <span class="play"><svg width="12" height="14" viewBox="0 0 12 14"><path d="M1 1l10 6-10 6z" fill="#fff"/></svg></span>
          </div></div>
          <div class="title">Lorem Ipsum dolor ism....</div>
          <div class="meta"><span>By Norvel</span><span>3 week ago</span></div>
        </article>
      </div>
    </div>
  </section>

  <!-- List results screen -->
  <section class="screen screen--list">
    <div class="status-bar">
      <span class="signal"><i style="height:3px"></i><i style="height:4px"></i><i style="height:5px"></i><i style="height:6px"></i><i style="height:7px"></i></span>
      <span class="carrier">QUIVEL</span><span class="net">3G</span>
      <svg class="lock" width="10" height="12" viewBox="0 0 10 12"><path d="M2.5 5V3.5a2.5 2.5 0 0 1 5 0V5" fill="none" stroke="#fff" stroke-width="1.5"/><rect x="1" y="5" width="8" height="7" rx="1" fill="#fff"/></svg>
      <span class="battery"></span>
    </div>
    <header class="app-header">
      <h1>Label</h1>
      <div class="toggle"><svg class="tick" width="20" height="20" viewBox="0 0 20 20"><path d="M3 10l5 5 9-11" fill="none" stroke="var(--green)" stroke-width="4" stroke-linecap="round"/></svg><span class="knob">‹ ›</span></div>
    </header>
    <div class="search-band">
      <div class="search-field filled"><svg width="11" height="11" viewBox="0 0 11 11"><circle cx="4.5" cy="4.5" r="3.5" fill="none" stroke="#555" stroke-width="1.4"/><path d="M7 7l3.5 3.5" stroke="#555" stroke-width="1.6"/></svg>Lorem Ipsum |</div>
    </div>
    <div class="list-body">
      <article class="list-item" style="top:7px">
        <div class="photo small ph-window" role="img" aria-label="Video thumbnail: figure behind a window grid">
          <span class="badge like"><svg width="7" height="6" viewBox="0 0 10 9"><path d="M5 9L1 5a2.5 2.5 0 0 1 4-3 2.5 2.5 0 0 1 4 3z" fill="#fff"/></svg></span>
          <span class="badge chat"><svg width="7" height="6" viewBox="0 0 10 9"><ellipse cx="5" cy="4" rx="4.5" ry="3.5" fill="#fff"/></svg></span>
          <span class="duration">4.06</span>
          <span class="play"><svg width="10" height="12" viewBox="0 0 12 14"><path d="M1 1l10 6-10 6z" fill="#fff"/></svg></span>
        </div>
        <div class="copy"><h2>LOREM IPSUM</h2><p>Lorem ipsum dolor sit amet, consectetur adipis-<br>icing elit, sed do eiusmod tempor incididunt ut<br>labore et dolore magna aliqua.</p><div class="by">By Norvel</div></div>
        <div class="stats"><span class="stat">◉ 725,23</span><span class="stat">▦ 12 June 2013</span></div>
      </article>
      <article class="list-item" style="top:108px">
        <div class="photo small ph-sea" role="img" aria-label="Video thumbnail: bicycle on a beach under a blue sky">
          <span class="badge like"><svg width="7" height="6" viewBox="0 0 10 9"><path d="M5 9L1 5a2.5 2.5 0 0 1 4-3 2.5 2.5 0 0 1 4 3z" fill="#fff"/></svg></span>
          <span class="badge chat"><svg width="7" height="6" viewBox="0 0 10 9"><ellipse cx="5" cy="4" rx="4.5" ry="3.5" fill="#fff"/></svg></span>
          <span class="duration">4.06</span>
          <span class="play"><svg width="10" height="12" viewBox="0 0 12 14"><path d="M1 1l10 6-10 6z" fill="#fff"/></svg></span>
        </div>
        <div class="copy"><h2>LOREM IPSUM</h2><p>Lorem ipsum dolor sit amet, consectetur adipis-<br>icing elit, sed do eiusmod tempor incididunt ut<br>labore et dolore magna aliqua.</p><div class="by">By Norvel</div></div>
        <div class="stats"><span class="stat">◉ 725,23</span><span class="stat">▦ 12 June 2013</span></div>
      </article>
      <article class="list-item" style="top:209px">
        <div class="photo small ph-kitchen" role="img" aria-label="Video thumbnail: two cooks in a kitchen">
          <span class="badge like"><svg width="7" height="6" viewBox="0 0 10 9"><path d="M5 9L1 5a2.5 2.5 0 0 1 4-3 2.5 2.5 0 0 1 4 3z" fill="#fff"/></svg></span>
          <span class="badge chat"><svg width="7" height="6" viewBox="0 0 10 9"><ellipse cx="5" cy="4" rx="4.5" ry="3.5" fill="#fff"/></svg></span>
          <span class="duration">4.06</span>
          <span class="play"><svg width="10" height="12" viewBox="0 0 12 14"><path d="M1 1l10 6-10 6z" fill="#fff"/></svg></span>
        </div>
        <div class="copy"><h2>LOREM IPSUM</h2><p>Lorem ipsum dolor sit amet, consectetur adipis-<br>icing elit, sed do eiusmod tempor incididunt ut<br>labore et dolore magna aliqua.</p><div class="by">By Norvel</div></div>
        <div class="stats"><span class="stat">◉ 725,23</span><span class="stat">▦ 12 June 2013</span></div>
      </article>
      <article class="list-item" style="top:311px">
        <div class="photo small ph-road" role="img" aria-label="Video thumbnail: autumn path through trees">
          <span class="badge like"><svg width="7" height="6" viewBox="0 0 10 9"><path d="M5 9L1 5a2.5 2.5 0 0 1 4-3 2.5 2.5 0 0 1 4 3z" fill="#fff"/></svg></span>
          <span class="badge chat"><svg width="7" height="6" viewBox="0 0 10 9"><ellipse cx="5" cy="4" rx="4.5" ry="3.5" fill="#fff"/></svg></span>
          <span class="duration">4.06</span>
          <span class="play"><svg width="10" height="12" viewBox="0 0 12 14"><path d="M1 1l10 6-10 6z" fill="#fff"/></svg></span>
        </div>
        <div class="copy"><h2>LOREM IPSUM</h2><p>Lorem ipsum dolor sit amet, consectetur adipis-<br>icing elit, sed do eiusmod tempor incididunt ut<br>labore et dolore magna aliqua.</p><div class="by">By Norvel</div></div>
        <div class="stats"><span class="stat">◉ 725,23</span><span class="stat">▦ 12 June 2013</span></div>
      </article>
    </div>
    <nav class="tab-bar">
      <div class="tab"><svg width="20" height="20" viewBox="0 0 20 20"><circle cx="10" cy="10" r="6" fill="none" stroke="#bbb" stroke-width="4" stroke-dasharray="3 2.3"/><circle cx="10" cy="10" r="4.5" fill="#bbb"/><circle cx="10" cy="10" r="2" fill="#2b2b2b"/></svg>Setting</div>
      <div class="tab"><svg width="22" height="16" viewBox="0 0 22 16"><path d="M1 8Q11-3 21 8Q11 19 1 8z" fill="#ccc"/><circle cx="11" cy="8" r="4" fill="#2b2b2b"/><circle cx="11" cy="8" r="2" fill="#ccc"/></svg>Recently Viewed</div>
      <div class="tab active"><svg width="36" height="16" viewBox="0 0 36 16"><path d="M1 8Q10-2 19 8Q10 18 1 8zM17 8Q26-2 35 8Q26 18 17 8z" fill="none" stroke="#ccc" stroke-width="2"/><circle cx="10" cy="8" r="3" fill="#ccc"/><circle cx="26" cy="8" r="3" fill="#ccc"/></svg>Most Viewed</div>
      <div class="tab"><svg width="18" height="18" viewBox="0 0 18 18"><circle cx="7" cy="7" r="5" fill="none" stroke="#bbb" stroke-width="2"/><path d="M11 11l6 6" stroke="#bbb" stroke-width="3" stroke-linecap="round"/></svg>Search</div>
      <div class="tab"><svg width="22" height="19" viewBox="0 0 22 19"><path d="M11 19L2 10A5.5 5.5 0 0 1 11 3a5.5 5.5 0 0 1 9 7z" fill="#ccc"/></svg>Favourites</div>
    </nav>
  </section>

</div>
</body>
</html>
```